Staffing Firm - Business Cards and Stationary
Business Cards, Letterhead, Envelopes and Brochure Layout
I need double sided standard sized Business Card [3.5" x 2"]
Use whatever fonts that you think are best.
Professional
Todd Dunlap
President/CEO
2250 North Birch Avenue, Ste 730
Lakeport, TX 75990
Direct Line - 832-555-0143
tdunlap@kelvor.com
www.kelvor.com
We would like them to be memorable but professional.
Possibly put the various divisions?
We will need layouts for each group/division.

```html
<!DOCTYPE html>
<html lang="en">
<head>
<meta charset="utf-8">
<title>Kelvor Staffing – Business Cards</title>
<link rel="stylesheet" href="https://fonts.googleapis.com/css2?family=Cinzel:wght@500&family=Arimo:wght@400;700&display=swap">
<style>
  :root{
    --backdrop:#e9e6e1;
    --card-white:#ffffff;
    --card-black:#0d0d0d;
    --card-black-2:#262626;
    --ink:#333333;
    --ink-soft:#666666;
    --logo-dark:#3a3a3a;
    --logo-light:#e6e6e6;
    --silver:#9a9a9a;
    --green:#3c7a3a;
    --purple:#7a2f7a;
    --red:#b3202a;
    --blue:#2f5f9e;
  }
  *{box-sizing:border-box;margin:0;padding:0}
  html,body{width:1200px;height:850px;overflow:hidden}
  body{background:var(--backdrop);font-family:"Arimo",Arial,sans-serif;color:var(--ink)}
  .card-sheet{
    position:absolute;left:329px;top:26px;
    display:grid;grid-template-columns:264px 264px;
    column-gap:12px;row-gap:13px;
  }
  .card{width:264px;height:148px;position:relative;overflow:hidden;box-shadow:0 2px 5px rgba(0,0,0,.25)}
  .row-silver{--accent:var(--silver)}
  .row-green{--accent:var(--green)}
  .row-purple{--accent:var(--purple)}
  .row-red{--accent:var(--red)}
  .row-blue{--accent:var(--blue)}

  .card-front{background:var(--card-white)}
  .card-front .brand{position:absolute;left:12px;top:12px;display:flex;align-items:center;gap:6px}
  .brand-mark{width:9px;height:9px;background:var(--accent);flex:none}
  .brand-name{font-family:"Cinzel",serif;font-weight:500;font-size:12px;letter-spacing:.5px;color:var(--logo-dark);line-height:1;white-space:nowrap}
  .division{position:absolute;left:27px;top:28px;font-size:5px;color:var(--accent);letter-spacing:.3px;white-space:nowrap}
  .contact{position:absolute;left:140px;top:34px;font-size:5px;line-height:7px;color:var(--ink-soft);white-space:nowrap}
  .contact .person{font-size:8.5px;line-height:10px;color:var(--ink)}
  .contact .role{font-size:5.5px;font-weight:700;color:var(--ink);margin-bottom:5px}
  .contact dl{display:grid;grid-template-columns:26px auto;margin-top:3px}
  .contact dt,.contact dd{line-height:7px}
  .accent-bar{position:absolute;left:0;right:0;bottom:0;height:7px;
    background:linear-gradient(90deg,transparent 0%,var(--accent) 45%,var(--accent) 100%)}

  .card-back{background:radial-gradient(ellipse at 40% 40%,var(--card-black-2),var(--card-black) 75%)}
  .card-back .brand{position:absolute;left:0;right:0;top:50px;display:flex;justify-content:center;align-items:center;gap:9px}
  .card-back .brand-mark{width:13px;height:13px}
  .card-back .brand-name{font-size:19px;color:var(--logo-light);letter-spacing:1px}
  .card-back .tagline{position:absolute;left:0;right:0;top:76px;text-align:center;font-size:8px;letter-spacing:2px;color:var(--logo-light)}
  .web-strip{position:absolute;left:0;right:0;bottom:0;height:12px;
    background:linear-gradient(90deg,transparent,var(--accent) 25%,var(--accent) 75%,transparent);
    font-size:5.5px;line-height:12px;text-align:center;color:#fff}
</style>
</head>
<body>
<main class="card-sheet">

  <article class="card card-front row-silver">
    <div class="brand"><span class="brand-mark"></span><span class="brand-name">Kelvor Staffing</span></div>
    <p class="division">staffing solutions</p>
    <div class="contact">
      <p class="person">Todd Dunlap</p><p class="role">President/CEO</p>
      <p>2250 North Birch Avenue, Ste 730</p><p>Lakeport, TX 75990</p>
      <dl><dt>Toll free</dt><dd>1-800-555-0199</dd><dt>Direct</dt><dd>832-555-0143</dd><dt>Phone</dt><dd>713-555-0122</dd><dt>Cell</dt><dd>281-555-0175</dd><dt>Fax</dt><dd>832-555-0188</dd><dt>Email</dt><dd>tdunlap@kelvor.com</dd></dl>
    </div>
    <div class="accent-bar"></div>
  </article>
  <article class="card card-back row-silver">
    <div class="brand"><span class="brand-mark"></span><span class="brand-name">Kelvor Staffing</span></div>
    <p class="tagline">staffing solutions</p>
    <p class="web-strip">www.kelvor.com</p>
  </article>

  <article class="card card-front row-green">
    <div class="brand"><span class="brand-mark"></span><span class="brand-name">Kelvor Staffing</span></div>
    <p class="division">medical staffing group</p>
    <div class="contact">
      <p class="person">Todd Dunlap</p><p class="role">President/CEO</p>
      <p>2250 North Birch Avenue, Ste 730</p><p>Lakeport, TX 75990</p>
      <dl><dt>Toll free</dt><dd>1-800-555-0199</dd><dt>Direct</dt><dd>832-555-0143</dd><dt>Phone</dt><dd>713-555-0122</dd><dt>Cell</dt><dd>281-555-0175</dd><dt>Fax</dt><dd>832-555-0188</dd><dt>Email</dt><dd>tdunlap@kelvor.com</dd></dl>
    </div>
    <div class="accent-bar"></div>
  </article>
  <article class="card card-back row-green">
    <div class="brand"><span class="brand-mark"></span><span class="brand-name">Kelvor Staffing</span></div>
    <p class="tagline">staffing solutions</p>
    <p class="web-strip">www.kelvor.com</p>
  </article>

  <article class="card card-front row-purple">
    <div class="brand"><span class="brand-mark"></span><span class="brand-name">Kelvor Staffing</span></div>
    <p class="division">professional services group</p>
    <div class="contact">
      <p class="person">Todd Dunlap</p><p class="role">President/CEO</p>
      <p>2250 North Birch Avenue, Ste 730</p><p>Lakeport, TX 75990</p>
      <dl><dt>Toll free</dt><dd>1-800-555-0199</dd><dt>Direct</dt><dd>832-555-0143</dd><dt>Phone</dt><dd>713-555-0122</dd><dt>Cell</dt><dd>281-555-0175</dd><dt>Fax</dt><dd>832-555-0188</dd><dt>Email</dt><dd>tdunlap@kelvor.com</dd></dl>
    </div>
    <div class="accent-bar"></div>
  </article>
  <article class="card card-back row-purple">
    <div class="brand"><span class="brand-mark"></span><span class="brand-name">Kelvor Staffing</span></div>
    <p class="tagline">staffing solutions</p>
    <p class="web-strip">www.kelvor.com</p>
  </article>

  <article class="card card-front row-red">
    <div class="brand"><span class="brand-mark"></span><span class="brand-name">Kelvor Staffing</span></div>
    <p class="division">staffing services group</p>
    <div class="contact">
      <p class="person">Todd Dunlap</p><p class="role">President/CEO</p>
      <p>2250 North Birch Avenue, Ste 730</p><p>Lakeport, TX 75990</p>
      <dl><dt>Toll free</dt><dd>1-800-555-0199</dd><dt>Direct</dt><dd>832-555-0143</dd><dt>Phone</dt><dd>713-555-0122</dd><dt>Cell</dt><dd>281-555-0175</dd><dt>Fax</dt><dd>832-555-0188</dd><dt>Email</dt><dd>tdunlap@kelvor.com</dd></dl>
    </div>
    <div class="accent-bar"></div>
  </article>
  <article class="card card-back row-red">
    <div class="brand"><span class="brand-mark"></span><span class="brand-name">Kelvor Staffing</span></div>
    <p class="tagline">staffing solutions</p>
    <p class="web-strip">www.kelvor.com</p>
  </article>

  <article class="card card-front row-blue">
    <div class="brand"><span class="brand-mark"></span><span class="brand-name">Kelvor Staffing</span></div>
    <p class="division">technology services group</p>
    <div class="contact">
      <p class="person">Todd Dunlap</p><p class="role">President/CEO</p>
      <p>2250 North Birch Avenue, Ste 730</p><p>Lakeport, TX 75990</p>
      <dl><dt>Toll free</dt><dd>1-800-555-0199</dd><dt>Direct</dt><dd>832-555-0143</dd><dt>Phone</dt><dd>713-555-0122</dd><dt>Cell</dt><dd>281-555-0175</dd><dt>Fax</dt><dd>832-555-0188</dd><dt>Email</dt><dd>tdunlap@kelvor.com</dd></dl>
    </div>
    <div class="accent-bar"></div>
  </article>
  <article class="card card-back row-blue">
    <div class="brand"><span class="brand-mark"></span><span class="brand-name">Kelvor Staffing</span></div>
    <p class="tagline">staffing solutions</p>
    <p class="web-strip">www.kelvor.com</p>
  </article>

</main>
</body>
</html>
```